Flyer-Design für Hundeschule
Zielgruppe
Ich habe eine Hundeschule, seit 11 Jahren, die sich gerade neu aufstellt. Meine Zielgruppe sind junge bis mittel alte Hundemenschen die ihren Hund erziehen möchten und gerne auch ihr Freizeit mit ihm verbringen.
Aufgabenstellung
Ich möchte gerne ein Design was Neukunden anspricht.
Gerne auch, was man sich an den Kühlschrank hängt, weil es so schön ist ;-)
Ich habe sehr viele Fotos vom Profi und kann immer nachliefern, falls deiner Meinung nach etwas nicht ganz passt.
Das Logo habe ich in allen möglichen Dateiformen. Kann ich auch gerne nachliefern.
Vielleicht ist es auch zu viel Text?
Ich bin für alles offen :-)
Die Flyer möchte ich dann bei papier-flott-shop.de bestellen.
Ich freue mich auf deinen Vorschlag!

```html
<!DOCTYPE html>
<html lang="de">
<head>
<meta charset="utf-8">
<title>PfotenPfad – Hundetraining für jede Schnauze</title>
<link href="https://fonts.googleapis.com/css2?family=Open+Sans:ital,wght@0,400;0,600;0,700;1,400&family=Kaushan+Script&display=swap" rel="stylesheet">
<style>
  :root{
    --bg:#e4e4e6;
    --paper:#f6f6f6;
    --teal:#86c0bc;
    --red:#c8402b;
    --ink:#3d3d3d;
    --ink-soft:#555;
    --sepia-a:#d9c7b3;
    --sepia-b:#6e5a48;
  }
  *{box-sizing:border-box;margin:0;padding:0}
  html,body{width:1200px;height:1134px;overflow:hidden}
  body{background:var(--bg);font-family:"Open Sans",Arial,sans-serif;color:var(--ink);position:relative}

  .spread{position:absolute;left:40px;width:1120px;display:flex;box-shadow:0 6px 18px rgba(0,0,0,.12)}
  .spread--outer{top:24px;height:520px}
  .spread--inner{top:574px;height:536px}
  .page{position:relative;width:560px;height:100%;background:var(--paper);overflow:hidden}

  /* outer spread – about page */
  .paw-trail{position:absolute;left:20px;top:40px;width:250px;height:440px;border-radius:20px;
    background:linear-gradient(160deg,rgba(192,122,92,.28),rgba(192,122,92,.12))}
  .portrait{position:absolute;left:300px;top:28px;width:230px;height:230px;border-radius:50%;
    background:radial-gradient(circle at 45% 40%,var(--sepia-a),var(--sepia-b));
    border:4px solid #fff;box-shadow:0 3px 10px rgba(0,0,0,.25);z-index:2}
  .about-box{position:absolute;left:110px;top:210px;width:430px;height:290px;background:var(--teal);
    border-radius:18px;padding:74px 54px 20px;text-align:center;color:#2f3a3a;font-size:12px;line-height:1.55}
  .about-box p{margin-bottom:8px}
  .chev{position:absolute;width:26px;height:22px}
  .chev--right{left:16px;top:160px}
  .chev--left{right:16px;top:64px}
  .signature{font-family:"Kaushan Script",cursive;color:var(--red);font-size:26px;margin-top:6px}

  /* outer spread – cover */
  .cover-photo{position:absolute;inset:0;
    background:linear-gradient(180deg,#4a3a2e 0%,#6b5140 40%,#7a6a60 70%,#5d4f46 100%)}
  .brand-box{position:absolute;right:24px;bottom:36px;width:300px;height:110px;border-radius:14px;
    background:rgba(255,255,255,.82);display:flex;align-items:center;gap:16px;padding:0 22px}
  .brand-dot{width:44px;height:44px;border-radius:50%;background:var(--teal)}
  .brand-name{font-size:30px;font-weight:600;color:var(--red);line-height:1}
  .brand-tag{font-size:12px;color:var(--ink-soft);margin-top:6px}

  /* inner spread */
  .inner-left{padding:26px 28px 0 30px;font-size:10.6px;line-height:1.42}
  .inner-right{padding:40px 26px 0 24px;font-size:10.6px;line-height:1.42;display:flex;gap:18px}
  .col{flex:1}
  .h-red{color:var(--red);font-weight:700;font-size:11.4px;margin-bottom:2px}
  .inner p{margin-bottom:3px}
  .list{list-style:none;padding-left:12px;margin:2px 0 6px}
  .list li{position:relative;margin-bottom:3px}
  .list > li::before{content:"•";position:absolute;left:-11px}
  .sub{list-style:none;padding-left:12px}
  .note{font-style:italic}
  .course-row{display:flex;align-items:flex-start;gap:14px;margin-bottom:6px}
  .dog-photo{flex:0 0 150px;height:150px;margin-top:6px;border-radius:50%;
    background:radial-gradient(circle at 40% 40%,#c9b7a4,#8a9ea4);
    border:4px solid #fff;box-shadow:0 3px 8px rgba(0,0,0,.25)}
  .course-row .list{flex:1;margin:0}
  .band{position:absolute;left:0;right:0;bottom:0;height:34px;background:var(--teal);color:#fff;
    font-size:11px;display:flex;align-items:center;justify-content:center}
</style>
</head>
<body>

<section class="spread spread--outer">
  <div class="page about">
    <div class="paw-trail" role="img" aria-label="Spur aus Pfotenabdrücken in Terrakotta"></div>
    <div class="portrait" role="img" aria-label="Sepiafoto der Trainerin mit ihrem Hund"></div>
    <div class="about-box">
      <svg class="chev chev--left" viewBox="0 0 26 22"><path d="M12 2 3 11l9 9M24 2l-9 9 9 9" fill="none" stroke="var(--red)" stroke-width="4"/></svg>
      <svg class="chev chev--right" viewBox="0 0 26 22"><path d="M2 2l9 9-9 9M14 2l9 9-9 9" fill="none" stroke="var(--red)" stroke-width="4"/></svg>
      <p>Mein Name ist Marlene Kessler, geb. 1986 in Weimar.<br>Meine Leben teile ich mit meinem Mann, unserer Tochter und unseren vier Hunden und vier Katzen im schönen Lindenfeld. Seit 2009 bin ich Hundetrainerin aus Leidenschaft.</p>
      <p>Ich setze alles daran, dass Mensch und Hund durch meine Hilfe (wieder) ein Team werden.</p>
      <p>Ich freue mich auf dich und deine Fellnase(n)!<br>Liebe Grüße und hab eine gute Zeit,</p>
      <div class="signature">Marlene Kessler</div>
    </div>
  </div>
  <div class="page cover">
    <div class="cover-photo" role="img" aria-label="Foto einer Gruppe Hundehalter mit Hunden auf einem Waldweg"></div>
    <div class="brand-box">
      <div class="brand-dot"></div>
      <div>
        <div class="brand-name">PfotenPfad</div>
        <div class="brand-tag">Hundetraining für jede Schnauze</div>
      </div>
    </div>
  </div>
</section>

<section class="spread spread--inner">
  <div class="page inner inner-left">
    <p class="h-red">Exklusives Einzeltraining oder doch gemeinsam in einer Hundegruppe lernen?</p>
    <p>Ich biete dir eine individuelle Lösung.</p>
    <p class="h-red">Gemeinsam lernen macht Spaß und fördert das Sozialverhalten deines Hundes.</p>
    <ul class="list">
      <li><b>Welpenkurs:</b> Wir legen gemeinsam den optimalen Grundstein für einen sozialen und ruhigen Hund. – Anmeldung bis zur 14. Lebenswoche, Einstieg jederzeit möglich, Dauer 8 Wochen, Kursgebühr 120 € –</li>
    </ul>
    <div class="course-row">
      <div class="dog-photo" role="img" aria-label="Foto eines Hundes, der durch Wasser läuft"></div>
      <ul class="list">
        <li><b>Junghundkurs:</b> Zusammenwachsen und aus dem jungen Wilden einen tollen Begleiter machen. – Anmeldung ab dem 4.–10. Monat, Dauer: 12 Wochen, Einstieg alle 6 Wochen möglich, Kursgebühr 180 € –</li>
        <li><b>Benimm dich! - Kurs</b> – die vier Säulen des guten Benehmens in Perfektion.
          <ul class="sub">
            <li>• Modul 1: Sicherer Rückruf</li>
            <li>• Modul 2: Entspanntes gehen an der Leine</li>
            <li>• Modul 3: Führen und Folgen</li>
            <li>• Modul 4: Sitz-Platz-Bleib in Perfektion</li>
          </ul>
          – Anmeldung ab dem 10. Lebensmonat, Dauer 4 Wochen je Modul, Einstieg alle 4 Wochen möglich, Je Modul 60 €, alle Module zusammen 220 € –</li>
      </ul>
    </div>
    <p><b>Workshops:</b> Manchmal hat man nur dieses eine, ganz spezielle Thema mit seinem Hund. Und man möchte genau hieran trainieren. Dann sind meine Workshops genau das Richtige. Immer wieder gibt es neue Themen, wie zum Beispiel „Die andere Art der Leinenführung“ oder „Der perfekte Rückruf“. Wir trainieren hier in kleinen Gruppen, um dein Ziel zu erreichen.</p>
    <div class="band">Alle Kurse finden in 04923 Birkenau OT Lindenfeld statt.</div>
  </div>
  <div class="page inner inner-right">
    <div class="col">
      <p class="h-red">Lust auf Abenteuer und Spaß? Verbringe Zeit mit deinem Hund in meinen Beschäftigungskursen:</p>
      <ul class="list">
        <li><b>Crossdogging:</b> Du und dein Hund stellen sich wöchentlich neuen spannenden Aufgaben. Hier lernst du auch in Stresssituationen ruhig zu bleiben und deine</li>
        <li><b>Rally Obedience:</b> Geschicklichkeit und Gehorsam gepaart mit jeder Menge Spaß.</li>
        <li><b>Longieren:</b> Distanz schafft Nähe! Du arbeitest mit deinem Hund über die Distanz am Longierkreis. Ein toller Sport für den Aufbau einer harmonischen Bindung und Beziehung.</li>
      </ul>
      <p class="h-red">Exklusives Einzeltraining</p>
      <p>Im Einzeltraining liegt mein ganze Aufmerksamkeit nur bei dir und deinem Hund. Die Trainings finden je nach Art bei dir Zuhause oder in Birkenau/ OT Lindenfeld statt.</p>
      <ul class="list">
        <li><b>Problemhundtherapie:</b> Dein Hund kann nicht alleine bleiben, zeigt Aggressionen in jeglicher Ausprägung oder ist ein ängstlicher Hund? Dann bist du bei mir genau richtig. Zusammen suchen wir nach der Ursache</li>
      </ul>
    </div>
    <div class="col">
      <p>des Verhaltens, denn diese ist Auslöser des gezeigten Problems. Zusammen arbeiten wir uns Schritt für Schritt aus dem Problemverhalten heraus, hin zu einer harmonischen Mensch-Hund-Beziehung.<br><span class="note">(Training vorrangig bei dir Zuhause)</span></p>
      <ul class="list">
        <li><b>Grunderziehung für Hunde ab 6 Monaten:</b> Ich zeige dir, wie du deinen Hund zu einem perfekten Begleiter machen kannst. Egal ob du ihn gerade aus dem Tierheim adoptiert, von privat übernommen hast oder er schon länger bei dir ist. Die kleinen Probleme des Alltags (Leineziehen, anspringen o.ä) werden wir schnell lösen. Es ist nie zu spät für eine tolle Mensch-Hund-Beziehung.<br><span class="note">(Training vorrangig in Birkenau)</span></li>
        <li><b>Welpenerziehung:</b> Ich zeige dir, wie du eine gute Basis schaffst, in der sich dein Welpe sicher fühlen kann. Dabei spielt gute Sozialisation natürlich eine große Rolle. All das wirst du im meinem Training, zusammen mit deinem Hund lernen.<br><span class="note">(Training vorrangig in Birkenau)</span></li>
      </ul>
    </div>
    <div class="band"></div>
  </div>
</section>

</body>
</html>
```